Pest Control - Brolga Pest Management

Pest Control
Termites (white ants)
Cockroaches
Ants
Spiders
Bed Bugs
Rats & Mice
Bird Proofing
Termite Inspections
Termite Baiting
Pest Identification

Commercial Services
Integrated Pest Management
Scheduled Servicing
Stored Product Pest
Rodent & Bird Control

Pre - Construction
Physical Termite Barriers
Chemical Barrier Installation
Reticulation Termite Barriers

Industry/Entity Type

Construction

Contact Information for Business Card

Malcolm: 0412 738 261
Tess: 0419 582 047

```html
<!DOCTYPE html>
<html lang="en">
<head>
<meta charset="utf-8">
<title>Brolga Pest Management – Business Card</title>
<link rel="stylesheet" href="https://fonts.googleapis.com/css2?family=Roboto:wght@300;400&display=swap">
<style>
  :root {
    --card-black: #0c0d0e;
    --card-dark: #16181a;
    --brush-grey: #3a3c3f;
    --brand-red: #e3161b;
    --licence-red: #a5161a;
    --text-white: #ffffff;
    --text-soft: #d6d6d6;
    --ghost: rgba(255, 255, 255, 0.045);
  }
  * { margin: 0; padding: 0; box-sizing: border-box; }
  html, body {
    width: 1200px; height: 720px; overflow: hidden;
    background: var(--card-black);
  }
  .card {
    position: relative;
    width: 1200px; height: 720px; overflow: hidden;
    font-family: "Roboto", "Helvetica Neue", Arial, sans-serif;
    font-weight: 300;
    background:
      linear-gradient(100deg, transparent 55%, rgba(80,82,86,0.35) 82%, rgba(110,112,116,0.45) 100%),
      repeating-linear-gradient(0deg, rgba(255,255,255,0.012) 0 1px, transparent 1px 3px),
      linear-gradient(180deg, var(--card-dark), var(--card-black));
  }
  .ghost-name {
    position: absolute; left: 580px; top: 470px;
    font-size: 170px; font-weight: 300; letter-spacing: -2px;
    color: var(--ghost); white-space: nowrap;
  }
  .brand {
    position: absolute; left: 96px; top: 118px;
    color: var(--brand-red); font-weight: 300;
    display: flex; align-items: center; gap: 22px;
  }
  .brand-dot {
    width: 26px; height: 26px; border-radius: 50%;
    background: var(--brand-red); flex: none;
  }
  .brand-name { font-size: 74px; line-height: 0.98; letter-spacing: -1px; }
  .contacts {
    position: absolute; right: 148px; top: 118px;
    text-align: right;
  }
  .person-name {
    font-size: 27px; color: var(--text-soft); line-height: 34px;
  }
  .phone {
    font-size: 38px; color: var(--text-white); line-height: 44px;
    position: relative;
  }
  .phone-icon {
    position: absolute; right: -38px; top: 6px; width: 18px; height: 32px;
  }
  .licence {
    font-size: 27px; color: var(--licence-red); line-height: 40px;
    margin-bottom: 10px;
  }
  .email {
    position: absolute; right: 148px; top: 396px;
    font-size: 27px; color: var(--text-white);
  }
  .email-icon {
    position: absolute; right: -50px; top: 8px; width: 32px; height: 22px;
  }
  .services {
    position: absolute; left: 117px; top: 468px;
    list-style: none; font-size: 24px; color: var(--text-soft);
    line-height: 30.5px;
  }
  .services-title { padding-left: 30px; }
  .service { position: relative; padding-left: 30px; }
  .tick {
    position: absolute; left: 0; top: 7px; width: 20px; height: 18px;
  }
</style>
</head>
<body>
<main class="card">
  <div class="ghost-name" aria-hidden="true">Brolga</div>

  <div class="brand">
    <span class="brand-dot"></span>
    <span class="brand-name">Brolga Pest<br>Management</span>
  </div>

  <section class="contacts">
    <p class="person-name">Malcolm</p>
    <p class="phone">0412 738 261
      <svg class="phone-icon" viewBox="0 0 18 32" aria-hidden="true">
        <rect x="1" y="6" width="16" height="25" rx="2.5" fill="var(--brand-red)"/>
        <rect x="12" y="0" width="2.5" height="7" fill="var(--brand-red)"/>
        <rect x="4" y="9" width="10" height="7" fill="var(--card-black)"/>
        <g fill="var(--card-black)">
          <rect x="4" y="19" width="2.5" height="2"/><rect x="8" y="19" width="2.5" height="2"/><rect x="12" y="19" width="2" height="2"/>
          <rect x="4" y="23" width="2.5" height="2"/><rect x="8" y="23" width="2.5" height="2"/><rect x="12" y="23" width="2" height="2"/>
        </g>
      </svg>
    </p>
    <p class="licence">LIC No: 1007315926</p>

    <p class="person-name">Tess</p>
    <p class="phone">0419 582 047
      <svg class="phone-icon" viewBox="0 0 18 32" aria-hidden="true">
        <rect x="1" y="6" width="16" height="25" rx="2.5" fill="var(--brand-red)"/>
        <rect x="12" y="0" width="2.5" height="7" fill="var(--brand-red)"/>
        <rect x="4" y="9" width="10" height="7" fill="var(--card-black)"/>
        <g fill="var(--card-black)">
          <rect x="4" y="19" width="2.5" height="2"/><rect x="8" y="19" width="2.5" height="2"/><rect x="12" y="19" width="2" height="2"/>
          <rect x="4" y="23" width="2.5" height="2"/><rect x="8" y="23" width="2.5" height="2"/><rect x="12" y="23" width="2" height="2"/>
        </g>
      </svg>
    </p>
    <p class="licence">LIC No: 1009642735</p>
  </section>

  <p class="email">hello@brolgapest.com.au
    <svg class="email-icon" viewBox="0 0 32 22" aria-hidden="true">
      <rect x="0" y="0" width="32" height="22" fill="var(--brand-red)"/>
      <path d="M1 1 L16 13 L31 1 M1 21 L12 10 M31 21 L20 10" stroke="var(--card-black)" stroke-width="1.6" fill="none"/>
    </svg>
  </p>

  <ul class="services">
    <li class="services-title">Specialise in</li>
    <li class="service"><svg class="tick" viewBox="0 0 20 18" aria-hidden="true"><path d="M1 10 L7 16 L19 2" stroke="var(--brand-red)" stroke-width="4" fill="none" stroke-linecap="round" stroke-linejoin="round"/></svg>Termite Eradication</li>
    <li class="service"><svg class="tick" viewBox="0 0 20 18" aria-hidden="true"><path d="M1 10 L7 16 L19 2" stroke="var(--brand-red)" stroke-width="4" fill="none" stroke-linecap="round" stroke-linejoin="round"/></svg>Termite Inspections</li>
    <li class="service"><svg class="tick" viewBox="0 0 20 18" aria-hidden="true"><path d="M1 10 L7 16 L19 2" stroke="var(--brand-red)" stroke-width="4" fill="none" stroke-linecap="round" stroke-linejoin="round"/></svg>General Pest Treatments</li>
    <li class="service"><svg class="tick" viewBox="0 0 20 18" aria-hidden="true"><path d="M1 10 L7 16 L19 2" stroke="var(--brand-red)" stroke-width="4" fill="none" stroke-linecap="round" stroke-linejoin="round"/></svg>Installation Chemical Barriers</li>
    <li class="service"><svg class="tick" viewBox="0 0 20 18" aria-hidden="true"><path d="M1 10 L7 16 L19 2" stroke="var(--brand-red)" stroke-width="4" fill="none" stroke-linecap="round" stroke-linejoin="round"/></svg>Installation Reticulation Barriers</li>
  </ul>
</main>
</body>
</html>
```